Business Card Design

I am a Special Event Consultant,I arrange and organise Special Events - Product Launches,Sponsorship and Product Displays.

I would like the RTV to be a feature of the design with 'Special Event Services" underneath - keep it very simple but creative using this information. So it is just the letters "RTV" with Event Services underneath.

(Simple Colours - Silver, Black, Grey - no bright colours - We work for Valtoria Drenn,KDX, Lyndrel So it is class and classic.)

Only my Name and mobile on the front.

Contact Information for Business Card

FRONT
Tess Varnholt
Tel: 0436 218907

BACK
Email: tess@rtveventservices.example.au

2807 Wexbury Heights,83 Pollard Street
NORTHVALE.Vic.3158.

```html
<!DOCTYPE html>
<html lang="en">
<head>
<meta charset="utf-8">
<title>RTV Event Services – Business Card</title>
<link href="https://fonts.googleapis.com/css2?family=Oswald:wght@500;600&family=Open+Sans:wght@400&display=swap" rel="stylesheet">
<style>
  :root {
    --page-bg: #d9d6d0;
    --card-black: #141414;
    --card-edge: #2a2a2a;
    --silver: #d6d6d6;
    --silver-dim: #a9a9a9;
    --rule: #6d6d6d;
    --mark-grey: #4a4a4a;
  }
  * { margin: 0; padding: 0; box-sizing: border-box; }
  html, body {
    width: 1200px; height: 1023px; overflow: hidden;
    background: var(--page-bg);
  }
  .sheet {
    width: 1200px; height: 1023px;
    display: flex; flex-direction: column; align-items: center; justify-content: center;
    gap: 44px;
  }
  .card {
    position: relative;
    width: 740px; height: 452px;
    border-radius: 22px;
    background: radial-gradient(ellipse at 35% 30%, #2b2b2b 0%, var(--card-black) 65%);
    border: 1px solid var(--card-edge);
    color: var(--silver);
    overflow: hidden;
  }
  /* front */
  .front__identity {
    position: absolute; left: 0; right: 0; top: 196px;
    display: flex; align-items: center; gap: 24px;
  }
  .front__rule { flex: 1; height: 1px; background: var(--rule); }
  .front__name {
    font-family: 'Oswald', sans-serif; font-weight: 600;
    font-size: 52px; letter-spacing: 2px; line-height: 1;
    white-space: nowrap; color: var(--silver);
  }
  .front__role {
    position: absolute; left: 0; right: 0; top: 262px; text-align: center;
    font-family: 'Oswald', sans-serif; font-weight: 500;
    font-size: 22px; letter-spacing: 2px; color: var(--silver-dim);
  }
  .contact {
    position: absolute; display: flex; align-items: center; gap: 12px;
    font-family: 'Oswald', sans-serif; font-weight: 500;
    font-size: 30px; letter-spacing: 2px; color: var(--silver);
  }
  .contact--mobile { left: 40px; bottom: 36px; }
  .contact__icon { width: 26px; height: 26px; }
  /* back */
  .back__brand {
    position: absolute; left: 0; right: 0; top: 110px;
    display: flex; flex-direction: column; align-items: center;
  }
  .back__mark {
    font-family: 'Oswald', sans-serif; font-weight: 600;
    font-size: 120px; line-height: 1; letter-spacing: 8px;
    color: var(--mark-grey);
  }
  .back__tagline {
    margin-top: 10px;
    font-family: 'Oswald', sans-serif; font-weight: 600;
    font-size: 40px; line-height: 1; letter-spacing: 3px; color: var(--silver);
  }
  .back__online {
    position: absolute; left: 34px; top: 28px;
    font-family: 'Open Sans', sans-serif; font-size: 15px; line-height: 1.6;
    color: var(--silver-dim);
  }
  .back__address {
    position: absolute; right: 40px; bottom: 34px; text-align: right;
    font-family: 'Open Sans', sans-serif; font-size: 17px; line-height: 1.5;
    color: var(--silver-dim);
  }
</style>
</head>
<body>
<main class="sheet">
  <section class="card front">
    <div class="front__identity">
      <div class="front__rule"></div>
      <div class="front__name">TESS VARNHOLT</div>
      <div class="front__rule"></div>
    </div>
    <div class="front__role">MANAGING DIRECTOR</div>
    <div class="contact contact--mobile">
      <svg class="contact__icon" viewBox="0 0 26 26" aria-hidden="true">
        <rect x="0" y="0" width="26" height="26" rx="4" fill="#cfcfcf"/>
        <path d="M8 5 L11 8 L9.5 10.5 C10.5 13 13 15.5 15.5 16.5 L18 15 L21 18 L19 21 C12 21 5 14 5 7 Z" fill="#1a1a1a"/>
      </svg>
      <span>0436218907</span>
    </div>
  </section>

  <section class="card back">
    <div class="back__online">
      tess@rtveventservices.example.au<br>
      rtveventservices.example.au
    </div>
    <div class="back__brand">
      <div class="back__mark">RTV</div>
      <div class="back__tagline">EVENT SERVICES</div>
    </div>
    <div class="back__address">
      2807 Wexbury Heights<br>
      83 Pollard Street. NORTHVALE. Vic. 3158.
    </div>
  </section>
</main>
</body>
</html>
```